Werbebrief
Zielgruppe
Unsere Zielgruppe sind Geschäftsführer junger Unternehmen.
Hallo,
Wir benötigen einen "Werbebrief". Es ist jedoch weniger ein Brief, als viel mehr eine etwas größerer "Werbekarte" (diese soll 105 x 210mm groß sein).
Auf der Vorderseite soll folgender Text stehen:
Für Unternehmen, die gerne expandieren möchten
Auf der Rückseite soll folgender Link stehen:
www.tolvek-werk.de/Expandieren
Darunter soll folgendes stehen:
Ihr persönlicher Code: ABC123
Wichtig ist, dass wir den Code individuell ändern können, da jeder einen anderen Code bekommt.
Unser Logo und Corporate Farbe habe ich hochgeladen. Das Design sollte auf jeden Fall zu unserer Webseite passen (www.tolvek-werk.de)
Wir freuen uns auf Ihre Vorschläge.

```html
<!DOCTYPE html>
<html lang="de">
<head>
<meta charset="utf-8">
<title>Tolvek Werk – Werbekarte</title>
<link href="https://fonts.googleapis.com/css2?family=Arimo:wght@400;700&display=swap" rel="stylesheet">
<style>
  :root {
    --page-bg: #b9b9b9;
    --header-blue: #02447f;
    --body-blue: #24618f;
    --footer-blue: #00305e;
    --rule-dark: #0a2a4a;
    --rule-light: #3d77a6;
    --text-white: #ffffff;
    --code-bg: #ffffff;
    --code-border: #8a8a8a;
    --code-text: #000000;
  }
  html, body {
    margin: 0;
    padding: 0;
    width: 1200px;
    height: 1200px;
    overflow: hidden;
    background: var(--page-bg);
    font-family: "Arimo", Arial, sans-serif;
  }
  .canvas {
    position: relative;
    width: 1200px;
    height: 1200px;
  }
  .card {
    position: absolute;
    left: 238px;
    width: 714px;
    height: 357px;
    display: flex;
    flex-direction: column;
    background: var(--body-blue);
  }
  .card--front { top: 205px; }
  .card--back  { top: 636px; }

  .card__header {
    height: 60px;
    background: var(--header-blue);
    border-bottom: 2px solid var(--rule-light);
    display: flex;
    align-items: center;
    padding-left: 18px;
    box-sizing: border-box;
  }
  .brand {
    display: flex;
    align-items: center;
    gap: 12px;
    color: var(--text-white);
    font-size: 30px;
    font-weight: 400;
    letter-spacing: 0.2px;
  }
  .brand__dot {
    width: 16px;
    height: 16px;
    border-radius: 50%;
    background: var(--text-white);
  }

  .card__body {
    flex: 1;
    display: flex;
    flex-direction: column;
    align-items: center;
    justify-content: center;
    color: var(--text-white);
    text-align: center;
  }
  .card__footer {
    height: 60px;
    background: var(--footer-blue);
    border-top: 2px solid var(--rule-dark);
    box-sizing: border-box;
  }

  .headline {
    margin: 0 0 50px;
    font-size: 41px;
    font-weight: 400;
    line-height: 1.2;
  }
  .headline__x {
    font-weight: 700;
    font-style: italic;
    font-size: 54px;
    line-height: 0;
  }

  .back-content { margin-bottom: 20px; }
  .web-link {
    font-size: 23px;
    margin: 0 0 6px;
  }
  .code-line {
    display: flex;
    align-items: center;
    justify-content: center;
    gap: 12px;
    font-size: 30px;
    margin: 0;
  }
  .code-field {
    display: inline-block;
    width: 143px;
    height: 32px;
    line-height: 32px;
    background: var(--code-bg);
    border: 1px solid var(--code-border);
    color: var(--code-text);
    font-size: 21px;
    box-sizing: border-box;
  }
</style>
</head>
<body>
<main class="canvas">

  <section class="card card--front" aria-label="Vorderseite">
    <header class="card__header">
      <div class="brand"><span class="brand__dot"></span>Tolvek Werk</div>
    </header>
    <div class="card__body">
      <h1 class="headline">Für Unternehmen, die gerne<br>e<span class="headline__x">X</span>pandieren möchten</h1>
    </div>
    <footer class="card__footer"></footer>
  </section>

  <section class="card card--back" aria-label="Rückseite">
    <header class="card__header">
      <div class="brand"><span class="brand__dot"></span>Tolvek Werk</div>
    </header>
    <div class="card__body">
      <div class="back-content">
        <p class="web-link">www.tolvek-werk.de/Expandieren</p>
        <p class="code-line">Ihr persönlicher Code: <span class="code-field">ABC123</span></p>
      </div>
    </div>
    <footer class="card__footer"></footer>
  </section>

</main>
</body>
</html>
```